Kovrilex - presentation for a remote DBA team offering data platform management

We need a website design for wordpress site called Kovrilex.cz
We deliver remote database and data platform administration and development, oversee the database administrators, consult and train the personnel responsible for the database operations. The website should include several sections, home page with graphics elements supporting the name and service - remote dba work; blog section; service introduction and description, team introduction and description, download section for documents, presentations etc.

Target Market(s)

small and medium business companies requiring remote DBA service

Number of Pages Required

3 page

Font styles to use
Sans Serif

Colors

Designer to choose colors to be used in the design.

Requirements
Must have
• The website should have several sections to introduce the services, blog, team introduction, downloads

```html
<!DOCTYPE html>
<html lang="en">
<head>
<meta charset="utf-8">
<title>Kovrilex.cz – Remote DBA</title>
<link href="https://fonts.googleapis.com/css2?family=Oswald:wght@400;500;600&family=Raleway:wght@400;500;600;700&display=swap" rel="stylesheet">
<style>
:root{
  --green:#5ce01c;
  --green-dark:#49c10f;
  --ink:#1c1c1c;
  --text:#555b60;
  --topbar:#59636b;
  --soft:#f1f5f3;
  --footer:#1d1f20;
  --footer-text:#c9c9c9;
  --white:#ffffff;
}
*{box-sizing:border-box;margin:0;padding:0}
html,body{width:1200px;height:3475px;overflow:hidden}
body{position:relative;font-family:"Raleway",sans-serif;color:var(--text);background:var(--white)}
.abs{position:absolute}
.heading{font-family:"Oswald",sans-serif;font-weight:500;color:var(--ink);text-transform:uppercase}
.green{color:var(--green)}
.btn{position:absolute;background:var(--green);color:var(--white);font-family:"Oswald",sans-serif;font-size:15px;letter-spacing:.5px;display:flex;align-items:center;justify-content:center;gap:8px;text-transform:uppercase}
.section-title{position:absolute;left:0;width:1200px;text-align:center;font-size:34px}
.title-rule{position:absolute;left:560px;width:80px;height:3px;background:var(--green)}
.title-rule::after{content:"";position:absolute;left:20px;top:0;width:40px;height:3px;background:#3b3b3b}
.lead{position:absolute;left:320px;width:560px;text-align:center;font-size:13px;line-height:20px}

/* top bar */
.topbar{left:0;top:0;width:1200px;height:46px;background:var(--topbar);color:var(--white);font-size:12px}
.topbar .item{position:absolute;top:15px;display:flex;align-items:center;gap:6px}
.follow{position:absolute;left:834px;top:0;width:366px;height:46px;background:var(--green);display:flex;align-items:center;padding-left:36px;gap:10px;font-weight:700;font-size:12px}
.follow .dot{width:9px;height:9px;border-radius:50%;background:var(--white)}

/* nav */
.nav{left:0;top:46px;width:1200px;height:66px;background:var(--white)}
.brand{position:absolute;left:174px;top:16px;display:flex;align-items:center;gap:10px;font-family:"Oswald",sans-serif;font-size:30px;font-weight:500;color:var(--ink)}
.brand .mark{width:16px;height:16px;background:var(--green)}
.menu{position:absolute;left:578px;top:27px;display:flex;gap:44px;font-size:12px;font-weight:600;color:#333}

/* hero */
.hero{left:0;top:112px;width:1200px;height:483px;background:linear-gradient(180deg,#242a31 0%,#3b434c 45%,#596068 70%,#2b3036 100%)}
.hero h1{position:absolute;left:0;top:188px;width:1200px;text-align:center;font-family:"Oswald",sans-serif;font-weight:600;font-size:40px;color:var(--white);letter-spacing:1px}
.hero h2{position:absolute;left:0;top:242px;width:1200px;text-align:center;font-family:"Oswald",sans-serif;font-weight:500;font-size:22px;color:var(--white);letter-spacing:1px}
.arrow{position:absolute;top:212px;width:38px;height:38px;background:var(--green);transform:rotate(45deg)}

/* about */
.about-photo{left:174px;top:658px;width:340px;height:468px;border:8px solid var(--green);background:linear-gradient(160deg,#e7ecef,#b9c6cf 55%,#6f7d86)}
.about-title{left:588px;top:652px;font-size:34px}
.about-rule{left:588px;top:697px;width:440px;height:2px;background:#333}
.about-rule::before{content:"";position:absolute;left:0;top:-1px;width:90px;height:4px;background:var(--green)}
.about-text{left:588px;top:716px;width:440px;font-size:12.5px;line-height:20px}
.feature{position:absolute;left:588px;width:440px;height:70px}
.feature svg{position:absolute;left:0;top:2px}
.feature h3{position:absolute;left:58px;top:0;font-family:"Raleway",sans-serif;font-weight:700;font-size:16px;color:var(--ink)}
.feature p{position:absolute;left:58px;top:26px;width:380px;font-size:11.5px;line-height:17px}

/* services */
.services{left:0;top:1190px;width:1200px;height:733px;background:var(--soft)}
.card{position:absolute;width:269px;height:225px;background:var(--white);text-align:center}
.card svg{position:absolute;left:112px;top:40px}
.card h3{position:absolute;left:0;top:98px;width:100%;font-family:"Oswald",sans-serif;font-weight:500;font-size:17px;color:var(--ink)}
.card p{position:absolute;left:30px;top:132px;width:209px;font-size:11.5px;line-height:17px}
.card.active{background:var(--green)}
.card.active::before{content:"";position:absolute;inset:12px;border:3px solid var(--white)}
.card.active h3,.card.active p{color:var(--white)}

/* news */
.post{position:absolute;top:2127px;width:269px;height:333px;background:var(--white);box-shadow:0 2px 8px rgba(0,0,0,.06)}
.post .photo{position:absolute;left:0;top:0;width:269px;height:167px}
.post .meta{position:absolute;left:18px;top:155px;width:233px;height:28px;background:var(--green);color:var(--white);font-size:11px;font-weight:600;display:flex;align-items:center;justify-content:space-between;padding:0 12px}
.post h3{position:absolute;left:18px;top:204px;width:235px;font-family:"Raleway",sans-serif;font-weight:600;font-size:16px;line-height:20px;color:var(--ink);text-transform:uppercase}
.post p{position:absolute;left:18px;top:250px;width:235px;font-size:11.5px;line-height:17px}

/* team */
.team{left:0;top:2521px;width:1200px;height:572px;background:var(--soft)}
.member{position:absolute;top:2697px;width:194px;height:301px;background:var(--white);text-align:center}
.member .portrait{position:absolute;left:0;top:0;width:194px;height:218px}
.member h3{position:absolute;left:0;top:238px;width:100%;font-family:"Raleway",sans-serif;font-weight:700;font-size:15px;color:var(--ink)}
.member p{position:absolute;left:0;top:262px;width:100%;font-size:11px;color:var(--green-dark)}
.member .tab{position:absolute;left:-4px;top:70px;width:4px;height:60px;background:var(--green)}
.socials-side{position:absolute;left:0;top:54px;display:flex;flex-direction:column;gap:8px}
.socials-side span{width:18px;height:18px;background:var(--green)}

/* contact band */
.band{left:174px;top:3056px;width:852px;height:70px;background:var(--green);color:var(--white);z-index:2}
.band .col{position:absolute;top:14px;display:flex;gap:14px;align-items:center}
.band b{display:block;font-family:"Oswald",sans-serif;font-weight:500;font-size:14px}
.band small{font-size:11px}

/* footer */
.footer{left:0;top:3093px;width:1200px;height:382px;background:var(--footer);color:var(--footer-text)}
.footer h4{position:absolute;top:88px;font-family:"Oswald",sans-serif;font-weight:500;font-size:15px;color:var(--white);letter-spacing:.5px}
.footer .about{position:absolute;left:174px;top:126px;width:270px;font-size:12px;line-height:22px}
.footer .line{position:absolute;left:174px;top:256px;width:46px;height:2px;background:var(--green)}
.footer .copy{position:absolute;left:174px;top:308px;font-size:11px}
.addr{position:absolute;left:466px;top:126px;font-size:12px;line-height:20px}
.addr div{display:flex;align-items:center;gap:10px;margin-bottom:8px}
.social-row{position:absolute;left:466px;top:306px;display:flex;gap:12px}
.social-row span{width:32px;height:32px;border-radius:50%;background:var(--white)}
.field{position:absolute;left:758px;width:268px;border:1px solid #4a4d4f;font-size:11px;color:#9a9a9a;padding:9px 10px}
.submit{position:absolute;left:758px;top:311px;width:90px;height:28px;background:var(--white);color:var(--ink);font-family:"Oswald",sans-serif;font-size:13px;display:flex;align-items:center;justify-content:center}
</style>
</head>
<body>

<header class="abs topbar">
  <div class="item" style="left:174px">
    <svg width="10" height="13" viewBox="0 0 10 13"><path d="M5 0a5 5 0 0 0-5 5c0 4 5 8 5 8s5-4 5-8a5 5 0 0 0-5-5z" fill="#fff"/><circle cx="5" cy="5" r="2" fill="#59636b"/></svg>
    412 Linden Ave, Brookfield, OR, 4417
  </div>
  <div class="item" style="left:482px">
    <svg width="12" height="12" viewBox="0 0 12 12"><path d="M2 0l3 3-1.5 2a7 7 0 0 0 3.5 3.5L9 7l3 3-2 2C5 12 0 7 0 2z" fill="#fff"/></svg>
    +420-555-010-214, +420-555-010-733
  </div>
  <div class="follow">FOLLOW US : <span class="dot"></span><span class="dot"></span><span class="dot"></span><span class="dot"></span></div>
</header>

<nav class="abs nav">
  <div class="brand"><span class="mark"></span>KOVRILEX.CZ</div>
  <div class="menu"><span>HOME</span><span>SERVICES</span><span>BLOG</span><span>TEAM</span><span>DOWNLOAD</span></div>
  <svg class="abs" style="left:1012px;top:28px" width="14" height="14" viewBox="0 0 14 14"><circle cx="6" cy="6" r="4.5" fill="none" stroke="#888" stroke-width="1.6"/><path d="M9.5 9.5L13 13" stroke="#888" stroke-width="1.6"/></svg>
</nav>

<section class="abs hero" role="img" aria-label="Server room corridor with rows of data racks">
  <h1>WE DELIVER REMOTE <span class="green">DATABASE AND DATA</span></h1>
  <h2>PLATFORM ADMINISTRATION AND DEVELOPMENT</h2>
  <div class="btn" style="left:519px;top:336px;width:162px;height:42px">Learn more <span>→</span></div>
  <div class="arrow" style="left:43px"></div>
  <div class="arrow" style="left:1117px"></div>
  <svg class="abs" style="left:56px;top:223px" width="12" height="16" viewBox="0 0 12 16"><path d="M9 2L3 8l6 6" fill="none" stroke="#fff" stroke-width="2.5"/></svg>
  <svg class="abs" style="left:1131px;top:223px" width="12" height="16" viewBox="0 0 12 16"><path d="M3 2l6 6-6 6" fill="none" stroke="#fff" stroke-width="2.5"/></svg>
</section>

<section class="about-section">
  <div class="abs about-photo" role="img" aria-label="Two colleagues working together at a computer in an office"></div>
  <h2 class="abs heading about-title">About <span class="green">Kovrilex.cz</span></h2>
  <div class="abs about-rule"></div>
  <p class="abs about-text">Lorem Ipsum is simply dummy text of the printing and typesetting industry. Lorem Ipsum has been the industry's standard dummy text ever since the 1500s. Lorem Ipsum is simply dummy text.</p>

  <div class="feature" style="top:792px">
    <svg width="42" height="30" viewBox="0 0 42 30"><path d="M10 28a9 9 0 0 1 0-18 12 12 0 0 1 22 2 8 8 0 0 1 0 16z" fill="#5ce01c"/></svg>
    <h3>CLOUD DBA</h3>
    <p>Sed ut perspiciatis unde omnis iste natus error sit voluptatem accusum doloremque laudantium.</p>
  </div>
  <div class="feature" style="top:876px">
    <svg width="42" height="40" viewBox="0 0 42 40"><circle cx="21" cy="8" r="6" fill="#5ce01c"/><path d="M12 38V22a9 9 0 0 1 18 0v16z" fill="#5ce01c"/><circle cx="7" cy="14" r="4" fill="#5ce01c"/><path d="M1 36V26a6 6 0 0 1 10-4v14z" fill="#5ce01c"/><circle cx="35" cy="14" r="4" fill="#5ce01c"/><path d="M41 36V26a6 6 0 0 0-10-4v14z" fill="#5ce01c"/></svg>
    <h3>EXPERT TEAM MEMBER</h3>
    <p>Sed ut perspiciatis unde omnis iste natus error sit voluptatem accusum doloremque laudantium.</p>
  </div>
  <div class="feature" style="top:964px">
    <svg width="42" height="36" viewBox="0 0 42 36"><rect x="2" y="2" width="38" height="24" fill="none" stroke="#5ce01c" stroke-width="3"/><path d="M8 20l7-8 6 5 7-9 6 6" fill="none" stroke="#5ce01c" stroke-width="2.5"/><path d="M14 34h14M21 26v8" stroke="#5ce01c" stroke-width="3"/></svg>
    <h3>DATABASE MONITORING</h3>
    <p>Sed ut perspiciatis unde omnis iste natus error sit voluptatem accusum doloremque laudantium.</p>
  </div>
  <div class="btn" style="left:593px;top:1075px;width:157px;height:44px">View details <span>→</span></div>
</section>

<section class="abs services">
  <h2 class="heading section-title" style="top:44px">Our <span class="green">Services</span></h2>
  <div class="title-rule" style="top:100px"></div>

  <div class="card" style="left:162px;top:133px">
    <svg width="44" height="44" viewBox="0 0 44 44"><ellipse cx="22" cy="9" rx="14" ry="5" fill="#5ce01c"/><path d="M8 12v8c0 3 6 5 14 5s14-2 14-5v-8c0 3-6 5-14 5S8 15 8 12zM8 24v8c0 3 6 5 14 5s14-2 14-5v-8c0 3-6 5-14 5S8 27 8 24z" fill="#5ce01c"/></svg>
    <h3>REMOTE DBA</h3>
    <p>Lorem Ipsum is simply dummy text of the printing and typesetting industry. Lorem Ipsum has.</p>
  </div>
  <div class="card active" style="left:465px;top:133px">
    <svg width="44" height="44" viewBox="0 0 44 44"><ellipse cx="20" cy="9" rx="13" ry="5" fill="#fff"/><path d="M7 12v8c0 3 6 5 13 5s13-2 13-5v-8c0 3-6 5-13 5S7 15 7 12zM7 24v8c0 3 6 5 13 5v-10c-7 0-13-2-13-3z" fill="#fff"/><circle cx="32" cy="32" r="8" fill="#fff"/><circle cx="32" cy="32" r="3" fill="#5ce01c"/></svg>
    <h3>CLUSTER DB</h3>
    <p>Lorem Ipsum is simply dummy text of the printing and typesetting industry. Lorem Ipsum has.</p>
  </div>
  <div class="card" style="left:769px;top:133px">
    <svg width="44" height="44" viewBox="0 0 44 44"><circle cx="22" cy="22" r="16" fill="none" stroke="#5ce01c" stroke-width="3"/><ellipse cx="22" cy="22" rx="7" ry="16" fill="none" stroke="#5ce01c" stroke-width="2.5"/><path d="M6 22h32M9 14h26M9 30h26" stroke="#5ce01c" stroke-width="2.5"/></svg>
    <h3>BUSINESS SUITE</h3>
    <p>Lorem Ipsum is simply dummy text of the printing and typesetting industry. Lorem Ipsum has.</p>
  </div>
  <div class="card" style="left:162px;top:388px">
    <svg width="44" height="44" viewBox="0 0 44 44"><circle cx="26" cy="22" r="14" fill="#5ce01c" opacity=".55"/><circle cx="20" cy="22" r="14" fill="#5ce01c"/><text x="20" y="28" text-anchor="middle" font-family="Oswald,sans-serif" font-size="17" fill="#fff">$</text></svg>
    <h3>PRICING</h3>
    <p>Lorem Ipsum is simply dummy text of the printing and typesetting industry. Lorem Ipsum has.</p>
  </div>
  <div class="card" style="left:465px;top:388px">
    <svg width="44" height="44" viewBox="0 0 44 44"><rect x="8" y="12" width="24" height="24" fill="none" stroke="#5ce01c" stroke-width="3"/><path d="M18 26l2-6 14-14 4 4-14 14z" fill="#5ce01c"/></svg>
    <h3>SERVICE LEVEL AGREEMENT</h3>
    <p>Lorem Ipsum is simply dummy text of the printing and typesetting industry. Lorem Ipsum has.</p>
  </div>
  <div class="card" style="left:769px;top:388px">
    <svg width="44" height="44" viewBox="0 0 44 44"><path d="M11 4h16l8 8v28H11z" fill="none" stroke="#5ce01c" stroke-width="3"/><path d="M23 14v14M17 22l6 6 6-6M16 34h14" fill="none" stroke="#5ce01c" stroke-width="3"/></svg>
    <h3>DOWNLOAD</h3>
    <p>Lorem Ipsum is simply dummy text of the printing and typesetting industry. Lorem Ipsum has.</p>
  </div>
  <div class="btn" style="left:519px;top:647px;width:162px;height:42px">View more <span>→</span></div>
</section>

<section class="news">
  <h2 class="heading section-title" style="top:1966px">Latest <span class="green">News</span></h2>
  <div class="title-rule" style="top:2022px"></div>
  <p class="lead" style="top:2040px">Lorem ipsum dolor sit amet adipiscing elit curabitur eu ante non lobortis posuere Lorem ipsum dolor sit amet adipiscing elit curabitur eu ante non lobortis posuere</p>

  <article class="post" style="left:174px">
    <div class="photo" role="img" aria-label="Man on the phone at a desk with computer screens" style="background:linear-gradient(135deg,#3f5a6b,#8aa0ad 60%,#d6c8a4)"></div>
    <div class="meta"><span>▣ 02.09.2018</span><span>▬ 3 Comment</span></div>
    <h3>There are many variations of passages</h3>
    <p>Lorem Ipsum is simply dummy text of the printing and typesetting industry. Lorem Ipsum has.</p>
  </article>
  <article class="post" style="left:466px">
    <div class="photo" role="img" aria-label="Group of colleagues celebrating around a laptop" style="background:linear-gradient(135deg,#5b5048,#a99a8b 55%,#e1dad2)"></div>
    <div class="meta"><span>▣ 02.09.2018</span><span>▬ 13 Comment</span></div>
    <h3>It is a long established fact that a reader</h3>
    <p>Lorem Ipsum is simply dummy text of the printing and typesetting industry. Lorem Ipsum has.</p>
  </article>
  <article class="post" style="left:758px">
    <div class="photo" role="img" aria-label="Hands typing on a laptop keyboard" style="background:linear-gradient(135deg,#2e4a6a,#6f8fb2 55%,#c6d4e2)"></div>
    <div class="meta"><span>▣ 01.09.2018</span><span>▬ 10 Comment</span></div>
    <h3>Contrary to popular belief, Lorem simply</h3>
    <p>Lorem Ipsum is simply dummy text of the printing and typesetting industry. Lorem Ipsum has.</p>
  </article>
</section>

<section class="abs team">
  <h2 class="heading section-title" style="top:38px">Our <span class="green">Team</span></h2>
  <div class="title-rule" style="top:94px"></div>
  <p class="lead" style="top:112px">Lorem ipsum dolor sit amet adipiscing elit curabitur eu ante non lobortis posuere Lorem ipsum dolor sit amet adipiscing elit curabitur eu ante non lobortis posuere</p>
</section>

<div class="member" style="left:174px">
  <div class="tab"></div>
  <div class="portrait" role="img" aria-label="Portrait of Marek Holub" style="background:linear-gradient(180deg,#fff,#e9e6e2)"></div>
  <h3>MAREK HOLUB</h3><p>Ceo &amp; Founder</p>
</div>
<div class="member" style="left:392px">
  <div class="portrait" role="img" aria-label="Portrait of Tomas Vrana" style="background:linear-gradient(180deg,#fff,#dfeef0)"></div>
  <div class="socials-side"><span></span><span></span><span></span></div>
  <h3>TOMAS VRANA</h3><p>Sr. Database Management</p>
</div>
<div class="member" style="left:612px">
  <div class="tab"></div>
  <div class="portrait" role="img" aria-label="Portrait of Karel Benes" style="background:linear-gradient(180deg,#fff,#e3e8ef)"></div>
  <h3>KAREL BENES</h3><p>Offshore Development</p>
</div>
<div class="member" style="left:832px">
  <div class="portrait" role="img" aria-label="Portrait of Lenka Dvorak" style="background:linear-gradient(180deg,#fff,#ecebea)"></div>
  <h3>LENKA DVORAK</h3><p>Human Resource</p>
</div>

<div class="abs band">
  <div class="col" style="left:34px">
    <svg width="34" height="26" viewBox="0 0 34 26"><rect x="1" y="1" width="32" height="24" fill="#fff"/><path d="M2 2l15 12L32 2" fill="none" stroke="#5ce01c" stroke-width="2.5"/></svg>
    <div><b>EMAIL</b><small>support@kovrilex.cz</small></div>
  </div>
  <div class="col" style="left:350px">
    <svg width="34" height="30" viewBox="0 0 34 30"><path d="M17 2C8 2 1 7 1 14c0 4 2 7 6 9l-2 6 8-4c1 0 3 .5 4 .5 9 0 16-5 16-11.5S26 2 17 2z" fill="#fff"/></svg>
    <div><b>LIVE CHAT 24/7</b><small>Reply time instantly</small></div>
  </div>
  <div class="col" style="left:626px">
    <svg width="28" height="28" viewBox="0 0 12 12"><path d="M2 0l3 3-1.5 2a7 7 0 0 0 3.5 3.5L9 7l3 3-2 2C5 12 0 7 0 2z" fill="#fff"/></svg>
    <div><b>PHONE</b><small>+420-555-010-214</small></div>
  </div>
</div>

<footer class="abs footer">
  <h4 style="left:174px">ABOUT US</h4>
  <p class="about">Lorem ipsum dolor sit amet, consectetur adipiscing elit. Aenean vel interdum tellus. Suspendisse leo libero, sollicitudin interdum tellus.</p>
  <div class="line"></div>
  <p class="copy">© 2018 Kovrilex.cz &nbsp; All Rights Reserved.</p>

  <h4 style="left:466px">ADDRESS</h4>
  <div class="addr">
    <div><svg width="10" height="13" viewBox="0 0 10 13"><path d="M5 0a5 5 0 0 0-5 5c0 4 5 8 5 8s5-4 5-8a5 5 0 0 0-5-5z" fill="#5ce01c"/></svg>412 Linden Ave, Brookfield, OR, 4417</div>
    <div><svg width="11" height="11" viewBox="0 0 12 12"><path d="M2 0l3 3-1.5 2a7 7 0 0 0 3.5 3.5L9 7l3 3-2 2C5 12 0 7 0 2z" fill="#5ce01c"/></svg>+420-555-010-214, +420-555-010-733</div>
    <div><svg width="12" height="9" viewBox="0 0 12 9"><rect width="12" height="9" fill="#5ce01c"/><path d="M0 0l6 5 6-5" fill="none" stroke="#1d1f20"/></svg>support@kovrilex.cz</div>
    <div><svg width="12" height="12" viewBox="0 0 12 12"><circle cx="6" cy="6" r="5.5" fill="#5ce01c"/></svg>www.kovrilex.cz</div>
  </div>
  <h4 style="left:466px;top:262px">CONNECT WITH US</h4>
  <div class="social-row"><span></span><span></span><span></span><span></span></div>

  <h4 style="left:758px">QUICK CONTACT</h4>
  <div class="field" style="top:132px;height:31px">Name</div>
  <div class="field" style="top:179px;height:31px">E-Mail</div>
  <div class="field" style="top:225px;height:65px">Message</div>
  <div class="submit">SUBMIT</div>
</footer>

</body>
</html>
```